Paintless Dent Company need a Fresh new look on a SUV partial wrap The company is named "Zarvo...

We are a Paintless Dent Company named Zarvo Auto.
Our logo is on our Facebook page. That logo needs to be on both sides along with 1. hail repair 2. ding and dent repair 3. 482-905-3164

```html
<!DOCTYPE html>
<html lang="en">
<head>
<meta charset="utf-8">
<title>Zarvo Auto – SUV Partial Wrap</title>
<link rel="stylesheet" href="https://fonts.googleapis.com/css2?family=Oswald:wght@400;500;600&display=swap">
<style>
  :root {
    --wrap-white: #ffffff;
    --wrap-red: #e10a0a;
    --ink: #111111;
    --panel-line: #d4d4d4;
    --phone-shadow: #8a8a8a;
  }
  html, body {
    margin: 0;
    padding: 0;
    width: 1200px;
    height: 1189px;
    overflow: hidden;
    background: var(--wrap-white);
    font-family: "Oswald", sans-serif;
  }
  .canvas {
    position: relative;
    width: 1200px;
    height: 1189px;
  }
  .wrap-art {
    position: absolute;
    inset: 0;
  }
  .phone {
    position: absolute;
    margin: 0;
    font-weight: 600;
    font-size: 52px;
    line-height: 1;
    letter-spacing: -1px;
    color: var(--wrap-red);
    white-space: nowrap;
    text-shadow:
      2px 0 0 #fff, -2px 0 0 #fff, 0 2px 0 #fff, 0 -2px 0 #fff,
      2px 2px 0 #fff, -2px -2px 0 #fff, 2px -2px 0 #fff, -2px 2px 0 #fff,
      4px 4px 0 var(--phone-shadow);
    transform: scaleY(1.15);
    transform-origin: left top;
  }
  .brand {
    position: absolute;
    display: flex;
    align-items: center;
    gap: 10px;
    white-space: nowrap;
  }
  .brand-dot {
    width: 20px;
    height: 20px;
    border-radius: 50%;
    background: var(--ink);
  }
  .brand-name {
    font-weight: 600;
    font-size: 32px;
    line-height: 1;
    color: var(--ink);
    letter-spacing: 2px;
  }
  .services {
    position: absolute;
    display: flex;
    align-items: center;
    gap: 14px;
    white-space: nowrap;
  }
  .service {
    display: flex;
    align-items: center;
    gap: 6px;
  }
  .service-icon {
    width: 36px;
    height: 36px;
  }
  .service-label {
    color: #fff;
    font-size: 16px;
    font-weight: 400;
    line-height: 1.1;
    text-transform: uppercase;
  }
</style>
</head>
<body>
<main class="canvas">
  <svg class="wrap-art" width="1200" height="1189" viewBox="0 0 1200 1189" aria-hidden="true">
    <rect x="50" y="250" width="1106" height="220" rx="18" fill="var(--wrap-white)" stroke="var(--panel-line)"/>
    <path d="M50,405 C200,395 330,385 380,378 C500,365 700,355 900,340 C1000,330 1060,318 1156,318 L1156,452 Q1156,470 1138,470 L68,470 Q50,470 50,452 Z" fill="var(--wrap-red)"/>
    <rect x="50" y="763" width="1106" height="220" rx="18" fill="var(--wrap-white)" stroke="var(--panel-line)"/>
    <path d="M1156,918 C1006,908 876,898 826,891 C706,878 506,868 306,853 C206,843 146,831 50,831 L50,965 Q50,983 68,983 L1138,983 Q1156,983 1156,965 Z" fill="var(--wrap-red)"/>
  </svg>

  <section class="side side-driver">
    <div class="brand" style="left:345px; top:370px;">
      <span class="brand-dot"></span>
      <span class="brand-name">ZARVO AUTO</span>
    </div>
    <p class="phone" style="left:616px; top:298px;">482-905-3164</p>
    <div class="services" style="left:596px; top:380px;">
      <div class="service">
        <svg class="service-icon" viewBox="0 0 38 38" aria-hidden="true">
          <circle cx="19" cy="19" r="17" fill="none" stroke="#fff" stroke-width="2"/>
          <path d="M10,25 L10,20 L13,15 L25,15 L28,20 L28,25 Z" fill="#fff"/>
          <path d="M17,8 L17,11 M19,7 L19,11 M21,8 L21,11" stroke="#fff" stroke-width="1"/>
        </svg>
        <span class="service-label">Hail<br>Repair</span>
      </div>
      <div class="service">
        <svg class="service-icon" viewBox="0 0 38 38" aria-hidden="true">
          <circle cx="19" cy="19" r="17" fill="none" stroke="#fff" stroke-width="2"/>
          <path d="M9,25 L9,19 L13,13 L25,13 L29,19 L29,25 Z" fill="#fff"/>
        </svg>
        <span class="service-label">Ding<br>and dent repair</span>
      </div>
    </div>
  </section>

  <section class="side side-passenger">
    <p class="phone" style="left:331px; top:806px;">482-905-3164</p>
    <div class="services" style="left:366px; top:882px;">
      <div class="service">
        <svg class="service-icon" viewBox="0 0 38 38" aria-hidden="true">
          <circle cx="19" cy="19" r="17" fill="none" stroke="#fff" stroke-width="2"/>
          <path d="M10,25 L10,20 L13,15 L25,15 L28,20 L28,25 Z" fill="#fff"/>
          <path d="M17,8 L17,11 M19,7 L19,11 M21,8 L21,11" stroke="#fff" stroke-width="1"/>
        </svg>
        <span class="service-label">Hail<br>Repair</span>
      </div>
      <div class="service">
        <svg class="service-icon" viewBox="0 0 38 38" aria-hidden="true">
          <circle cx="19" cy="19" r="17" fill="none" stroke="#fff" stroke-width="2"/>
          <path d="M9,25 L9,19 L13,13 L25,13 L29,19 L29,25 Z" fill="#fff"/>
        </svg>
        <span class="service-label">Ding<br>and dent repair</span>
      </div>
    </div>
    <div class="brand" style="left:645px; top:872px;">
      <span class="brand-dot"></span>
      <span class="brand-name">ZARVO AUTO</span>
    </div>
  </section>
</main>
</body>
</html>
```